Burlgrain Joinery eye catching business card

I need an eye catching business card that reflects my traditional, fun, handmade woodcraft shop. I make high end custom furniture and fine woodworking products, a lot of which are rustic, natural looking. We are a small shop but we produce awesome, one of a kind wood products, and our business card should reflect that. Our target audience is young professionals to retired folks who want a quality, local, handmade product. I'd like the Shop Nearby logo somewhere on the card, BUT not overwhelming, the main focus is my Logo, no preference on color whichever looks the best. Visit my website to get a feel for my company. Burlgrainjoinery.com
Target Market(s)
young professionals to retired folks. Any one who wants to furnish their home with quality handcrafted products.
Industry/Entity Type
Business
Contact Information for Business Card
Dale Merriwick (555)417-6293
dale@burlgrainjoinery.com
www.burlgrainjoinery.com

```html
<!DOCTYPE html>
<html lang="en">
<head>
<meta charset="utf-8">
<title>Burlgrain Joinery — Business Card</title>
<link href="https://fonts.googleapis.com/css2?family=Montserrat:wght@700&family=Questrial&display=swap" rel="stylesheet">
<style>
  :root {
    --backdrop: #e4e4e4;
    --card-dark: #141414;
    --card-light: #ffffff;
    --ink: #111111;
    --ink-soft: #3a3a3a;
    --paper-text: #ffffff;
    --photo-dark-a: #2a2522;
    --photo-dark-b: #0e0e0e;
    --photo-light-a: #f7f4f0;
    --photo-light-b: #ffffff;
  }
  * { box-sizing: border-box; margin: 0; padding: 0; }
  html, body { width: 1200px; height: 852px; overflow: hidden; }
  body {
    background: var(--backdrop);
    font-family: "Questrial", sans-serif;
    position: relative;
  }
  .card {
    position: absolute;
    top: 276px;
    width: 525px;
    height: 300px;
    border-radius: 22px;
    overflow: hidden;
    box-shadow: 0 6px 18px rgba(0,0,0,0.18);
  }
  /* Front */
  .card--front { left: 55px; background: var(--card-dark); }
  .card--front .photo {
    position: absolute; inset: 0;
    background: radial-gradient(ellipse at 40% 60%, var(--photo-dark-a) 0%, var(--photo-dark-b) 75%);
  }
  .card--front .brand {
    position: absolute; inset: 0;
    display: flex; align-items: center; justify-content: center;
    font-family: "Montserrat", sans-serif;
    font-weight: 700;
    font-size: 38px;
    letter-spacing: 2px;
    color: var(--paper-text);
    text-transform: uppercase;
  }
  /* Back */
  .card--back { left: 620px; background: var(--card-light); }
  .card--back .photo {
    position: absolute; inset: 0;
    background: linear-gradient(135deg, var(--photo-light-b) 30%, var(--photo-light-a) 100%);
  }
  .card--back .edge-band {
    position: absolute; left: 0; top: 0; bottom: 0;
    width: 34px; background: var(--card-dark);
  }
  .card--back .brand {
    position: absolute; right: 36px; top: 34px;
    font-family: "Montserrat", sans-serif;
    font-weight: 700;
    font-size: 19px;
    letter-spacing: 1px;
    color: var(--ink);
    text-transform: uppercase;
  }
  .person { position: absolute; left: 66px; top: 108px; }
  .person .name {
    font-family: "Montserrat", sans-serif;
    font-weight: 700; font-size: 21px; color: var(--ink);
  }
  .person .role { font-size: 15px; color: var(--ink-soft); margin-top: 2px; }
  .contacts {
    position: absolute; left: 66px; bottom: 34px;
    list-style: none;
  }
  .contacts li {
    display: flex; align-items: center; gap: 12px;
    font-size: 15px; color: var(--ink-soft); line-height: 26px;
  }
  .contacts svg { width: 13px; height: 13px; fill: var(--ink); flex: none; }
</style>
</head>
<body>
  <section class="card card--front">
    <div class="photo" role="img" aria-label="Dim workshop photo of a woodworker shaping wood at a bench"></div>
    <div class="brand">Burlgrain Joinery</div>
  </section>

  <section class="card card--back">
    <div class="photo" role="img" aria-label="Faint washed-out photo of woodworking hand tools"></div>
    <div class="edge-band"></div>
    <div class="brand">Burlgrain Joinery</div>
    <div class="person">
      <p class="name">Dale Merriwick</p>
      <p class="role">Owner</p>
    </div>
    <ul class="contacts">
      <li>
        <svg viewBox="0 0 16 16" aria-hidden="true"><path d="M3 1h3l1 4-2 1a9 9 0 0 0 5 5l1-2 4 1v3a2 2 0 0 1-2 2C7 15 1 9 1 3a2 2 0 0 1 2-2z"/></svg>
        (555)417-6293
      </li>
      <li>
        <svg viewBox="0 0 16 16" aria-hidden="true"><circle cx="8" cy="8" r="7" fill="none" stroke="#111" stroke-width="1.6"/><path d="M1 8h14M8 1c-3 4-3 10 0 14M8 1c3 4 3 10 0 14" fill="none" stroke="#111" stroke-width="1.2"/></svg>
        www.burlgrainjoinery.com
      </li>
      <li>
        <svg viewBox="0 0 16 16" aria-hidden="true"><path d="M1 3h14v10H1z"/><path d="M1 3l7 6 7-6" fill="none" stroke="#fff" stroke-width="1.3"/></svg>
        dale@burlgrainjoinery.com
      </li>
    </ul>
  </section>
</body>
</html>
```